Business Card for a Creative Technology based HR services company

Our company name is Leaf8, and we build large communities of HR (human resource) and finance personnels through our mobile platform, and we conduct lots of on-line and off-line activities to get everyone constantly connected. Behind all these, we will also provide on-site HR and finance contractors to our clients, plus a host of other HR-related services. No process in our company takes more than 5-steps.
Our company slogan: Touching Your Future
Target Market(s)
All human resource (HR) and finance personnels, from new entrants to highly experienced senior professionals.
Industry/Entity Type
Finance
Colors
Designer to choose colors to be used in the design.
Look and feel
Each slider illustrates characteristics of the customer's brand and the style your logo design should communicate.

```html
<!DOCTYPE html>
<html lang="en">
<head>
<meta charset="utf-8">
<title>Leaf8 Business Card</title>
<link rel="stylesheet" href="https://fonts.googleapis.com/css2?family=Lato:wght@400;700;900&family=Satisfy&display=swap">
<style>
  :root {
    --navy: #13294f;
    --red: #e41f2d;
    --white: #ffffff;
    --backdrop: #2b2b2b;
    --text-dark: #13294f;
  }
  html, body {
    margin: 0;
    padding: 0;
    width: 1200px;
    height: 900px;
    overflow: hidden;
    background: var(--backdrop);
  }
  .canvas {
    position: relative;
    width: 1200px;
    height: 900px;
  }
  .card {
    position: absolute;
    width: 700px;
    height: 400px;
    box-sizing: border-box;
    overflow: hidden;
  }
  .card-back {
    left: 80px;
    top: 50px;
    background: var(--navy);
    display: flex;
    align-items: center;
    justify-content: center;
  }
  .slogan {
    font-family: "Satisfy", cursive;
    color: var(--white);
    font-size: 64px;
    margin: 0;
  }
  .card-front {
    left: 420px;
    top: 460px;
    background: var(--white);
    color: var(--text-dark);
    font-family: "Lato", sans-serif;
  }
  .holder {
    position: absolute;
    right: 40px;
    top: 36px;
    text-align: right;
  }
  .holder-name {
    font-size: 22px;
    font-weight: 700;
    color: var(--navy);
    letter-spacing: 0.5px;
  }
  .holder-role {
    font-size: 16px;
    color: var(--red);
  }
  .brand {
    position: absolute;
    left: 40px;
    top: 110px;
    display: flex;
    align-items: center;
    gap: 14px;
  }
  .brand-dot {
    width: 26px;
    height: 26px;
    border-radius: 50%;
    background: var(--red);
  }
  .brand-name {
    font-size: 84px;
    font-weight: 900;
    color: var(--navy);
    line-height: 1;
  }
  .contacts {
    position: absolute;
    left: 40px;
    bottom: 44px;
    margin: 0;
    padding: 0;
    list-style: none;
    font-size: 17px;
    color: var(--navy);
  }
  .contacts li {
    display: flex;
    align-items: center;
    gap: 12px;
    margin-top: 6px;
  }
  .contacts svg {
    width: 14px;
    height: 14px;
    fill: var(--red);
    flex: none;
  }
  .edge-band {
    position: absolute;
    left: 0;
    bottom: 0;
    width: 700px;
    height: 40px;
  }
</style>
</head>
<body>
<div class="canvas">
  <section class="card card-back">
    <p class="slogan">Touching Your Future</p>
  </section>

  <section class="card card-front">
    <div class="holder">
      <div class="holder-name">YOUR NAME</div>
      <div class="holder-role">Director</div>
    </div>

    <div class="brand">
      <span class="brand-name">Leaf8</span>
      <span class="brand-dot"></span>
    </div>

    <ul class="contacts">
      <li>
        <svg viewBox="0 0 24 24"><path d="M6.6 10.8a15 15 0 0 0 6.6 6.6l2.2-2.2a1 1 0 0 1 1-.25 11.4 11.4 0 0 0 3.6.57 1 1 0 0 1 1 1V20a1 1 0 0 1-1 1A17 17 0 0 1 3 4a1 1 0 0 1 1-1h3.5a1 1 0 0 1 1 1c0 1.25.2 2.45.57 3.57a1 1 0 0 1-.25 1z"/></svg>
        1234 567 8901
      </li>
      <li>
        <svg viewBox="0 0 24 24"><path d="M2 5h20v14H2z M2 5l10 8 10-8" /></svg>
        yourname@leaf8.com.ca
      </li>
      <li>
        <svg viewBox="0 0 24 24"><path d="M12 2a7 7 0 0 0-7 7c0 5 7 13 7 13s7-8 7-13a7 7 0 0 0-7-7zm0 9.5A2.5 2.5 0 1 1 12 6.5a2.5 2.5 0 0 1 0 5z"/></svg>
        22 B Suite Maple Lane, ON 2020, Canada
      </li>
      <li>
        <svg viewBox="0 0 24 24"><circle cx="12" cy="12" r="10"/></svg>
        www.leaf8.com.ca
      </li>
    </ul>

    <svg class="edge-band" viewBox="0 0 700 40" preserveAspectRatio="none">
      <polygon points="0,30 700,10 700,40 0,40" fill="var(--navy)"/>
      <polygon points="620,12 700,10 700,18 612,20" fill="var(--red)"/>
    </svg>
  </section>
</div>
</body>
</html>
```